Quick Banner Ad Job for IT Services Company

Need a collection of banner ads based around a common theme and message.

Main Theme.

IT Support and Managed Services - IT support you can rely on.
Free remote monitoring and alerting*
*conditions apply <-- this in small text

Secondary Content

Our customers are attracted by our exceptional level of customer service and trust us in providing them with support and advice over a long term relationship.

Note:
* Logos and colours attached. Only use these colours.
* Font is to be Myriad Pro

* Delivery will require the following sizes.
Leaderboard: 728×90
Medium Rectangle: 300×250
Wide Skyscraper: 160×600

Do the initial draft in leaderboard, other sizes can be worked once we have an agreed design for the main

Final delivery will also need to be in an editable format, not just final images.

Industry/Entity Type

It Company

```html
<!DOCTYPE html>
<html lang="en">
<head>
<meta charset="UTF-8">
<title>TekNova IT Support – Leaderboard</title>
<link rel="stylesheet" href="https://fonts.googleapis.com/css2?family=Source+Sans+3:wght@400;600;700&display=swap">
<style>
  :root {
    --navy: #0f2a4a;
    --brand-blue: #1b6fb8;
    --sky: #bfe0f5;
    --sky-light: #e6f3fb;
    --cyan: #19b6e8;
    --white: #ffffff;
    --photo-warm: #e9d6c6;
    --photo-cool: #f4f1ee;
  }
  html, body {
    margin: 0;
    padding: 0;
    overflow: hidden;
    background: var(--white);
  }
  .banner {
    position: relative;
    width: 1200px;
    height: 148px;
    overflow: hidden;
    background: var(--white);
    font-family: "Source Sans 3", "Myriad Pro", sans-serif;
  }
  .banner__swoosh {
    position: absolute;
    left: 0;
    top: 0;
    width: 420px;
    height: 148px;
  }
  .brand {
    position: absolute;
    left: 30px;
    top: 28px;
    display: flex;
    align-items: center;
    gap: 16px;
  }
  .brand__dot {
    width: 74px;
    height: 74px;
    border-radius: 50%;
    background: var(--brand-blue);
  }
  .brand__name {
    font-size: 64px;
    font-weight: 700;
    color: var(--navy);
    line-height: 1;
    letter-spacing: -1px;
  }
  .brand__tagline {
    position: absolute;
    left: 300px;
    top: 102px;
    font-size: 18px;
    font-weight: 400;
    color: var(--navy);
  }
  .offer {
    position: absolute;
    left: 420px;
    top: 22px;
    width: 480px;
    text-align: center;
    color: var(--navy);
  }
  .offer__headline {
    margin: 0;
    font-size: 28px;
    font-weight: 600;
    line-height: 1.45;
  }
  .offer__terms {
    margin: 0;
    font-size: 26px;
    font-weight: 600;
    line-height: 1.45;
  }
  .banner__photo {
    position: absolute;
    right: 0;
    top: 0;
    width: 320px;
    height: 148px;
    background: linear-gradient(90deg, var(--white) 0%, var(--photo-cool) 25%, var(--photo-warm) 60%, var(--photo-cool) 100%);
  }
  .cta {
    position: absolute;
    right: 14px;
    bottom: 8px;
    font-size: 25px;
    font-weight: 700;
    color: var(--cyan);
    text-decoration: none;
  }
</style>
</head>
<body>
  <div class="banner">
    <svg class="banner__swoosh" viewBox="0 0 420 148" aria-hidden="true">
      <defs>
        <linearGradient id="swooshFade" x1="0" y1="0" x2="1" y2="0">
          <stop offset="0" stop-color="#bfe0f5"/>
          <stop offset="1" stop-color="#e6f3fb" stop-opacity="0"/>
        </linearGradient>
      </defs>
      <path d="M0 0 H300 C220 40 160 95 120 148 H0 Z" fill="url(#swooshFade)"/>
      <path d="M0 148 C60 110 140 70 260 0 H300 C200 55 140 100 100 148 Z" fill="#1b6fb8" opacity="0.18"/>
    </svg>

    <div class="brand">
      <span class="brand__dot"></span>
      <span class="brand__name">TekNova</span>
    </div>
    <div class="brand__tagline">IT Support</div>

    <div class="offer">
      <p class="offer__headline">Free remote monitoring and alerting</p>
      <p class="offer__terms">Conditions Apply</p>
    </div>

    <div class="banner__photo" role="img" aria-label="Photo of smiling support staff wearing headsets"></div>

    <a class="cta" href="#">click here</a>
  </div>
</body>
</html>
```